Plant Based Planner Graphics - Animals, Doctor Portraits & Charts

I am looking for a few custom graphics to use in a Plant Based Daily Planner. I would love some fun renditions of some famous plant based doctors to use on the pages featuring them. Then also a few plant inspired graphics that I can use throughout the planner. This is for print for sale.
Hoping to work with one designer on the entire project but please feel free to provide any one of the following graphics for me to consider you for the whole project.
~Doctors Likeness Graphics of:Dr. T.C. CampbellDr. EsselysteinDr. GregerDr. Owen Tashley
~Macro Ratio Pie Chart for Whole Food Plant Based showing 75-80% Carbs, 10-15% Fat and 10-15% Protein
~One graphic of someone sleeping dreaming about vegetables
~Cute graphic of a happy Fish, Honey Bee, Chicken and Cow - all separate graphics
~One Graphic of Kale, Spinach, Lettuce and Beet Greens - one graphic
~One Graphic of what Inflammation is associated with: Cardiovascular Disease, Diabetes, Arthritis, Autoimmune Disease, Lung Diseases, Neurological Diseases, Alzheimer Disease
~ One Simple Graphic Asking "Does it make sense to use 9 Plant Based Calories to make 1 Animal Based Calorie?"Would like to avoid harsh primary colors.
I included a suggest color palette. I am also using the font "quicksand" if that is an option. Attached Files are only inspiration.
Target Market(s)
20-15 Year Old Health and Environmental Conscious Readers
Font styles to use
Other font styles liked:
- Quicksand
Requirements
Should not have
- No depictions of Animal Food Products, Oil, or Processed Foods.

```html
<!DOCTYPE html>
<html lang="en">
<head>
<meta charset="utf-8">
<title>Plant vs Animal Calories</title>
<link rel="stylesheet" href="https://fonts.googleapis.com/css2?family=Quicksand:wght@700&display=swap">
<style>
  :root {
    --purple: #6a4499;
    --green: #b1d56b;
    --paper: #ffffff;
  }
  html, body {
    margin: 0;
    padding: 0;
    overflow: hidden;
    background: var(--paper);
  }
  .canvas {
    position: relative;
    width: 1200px;
    height: 1200px;
    background: var(--paper);
    font-family: "Quicksand", sans-serif;
    font-weight: 700;
    overflow: hidden;
  }
  .canvas p {
    position: absolute;
    margin: 0;
    white-space: nowrap;
    line-height: 1;
  }
  .lead {
    left: 126px;
    top: 240px;
    font-size: 78px;
    color: var(--purple);
  }
  .big-number {
    color: var(--purple);
    font-size: 380px;
    letter-spacing: -10px;
  }
  .big-number.nine { left: 118px; top: 300px; }
  .big-number.one { left: 128px; top: 612px; }
  .phrase {
    color: var(--green);
    font-size: 116px;
    letter-spacing: -1px;
  }
  .phrase.plant-1 { left: 330px; top: 362px; }
  .phrase.plant-2 { left: 330px; top: 472px; }
  .phrase.animal-1 { left: 336px; top: 674px; }
  .phrase.animal-2 { left: 336px; top: 784px; }
  .connector {
    left: 336px;
    top: 590px;
    font-size: 76px;
    color: var(--purple);
  }
</style>
</head>
<body>
  <main class="canvas">
    <p class="lead">Does it make sense to use</p>
    <p class="big-number nine">9</p>
    <p class="phrase plant-1">Plant Based</p>
    <p class="phrase plant-2">Calories</p>
    <p class="connector">to make</p>
    <p class="big-number one">1</p>
    <p class="phrase animal-1">Animal Based</p>
    <p class="phrase animal-2">Calorie?</p>
  </main>
</body>
</html>
```